Quelmira Business Card

Need a business card for our business.

Attached are our Logos. There is either the white and black all the all red with white. Either Logo can be used.

The winner will be provided the details for phone number and address.

Good Luck!

Business

```html
<!DOCTYPE html>
<html lang="en">
<head>
<meta charset="utf-8">
<title>Quelmira Industries – Business Card</title>
<link rel="stylesheet" href="https://fonts.googleapis.com/css2?family=Montserrat:wght@600;700&family=Questrial&display=swap">
<style>
  :root {
    --backdrop: #e9e6e1;
    --brand-red: #8c2a2c;
    --brand-red-dark: #6e2426;
    --brand-red-light: #a23033;
    --card-white: #f7f7f6;
    --ink: #3a3a3a;
    --ink-soft: #5c5c5c;
    --rule-grey: #8a8a8a;
    --band-grey: #9b9b9b;
  }
  * { margin: 0; padding: 0; box-sizing: border-box; }
  html, body {
    width: 1200px; height: 800px; overflow: hidden;
    background: var(--backdrop);
  }
  .canvas { position: relative; width: 1200px; height: 800px; }

  .card {
    position: absolute;
    box-shadow: 0 6px 18px rgba(0,0,0,0.18);
  }

  /* Front */
  .card-front {
    left: 170px; top: 280px; width: 556px; height: 282px;
    background:
      radial-gradient(ellipse 60% 70% at 58% 50%, var(--brand-red-light) 0%, var(--brand-red) 55%, var(--brand-red-dark) 100%);
    display: flex; align-items: center; justify-content: center;
  }
  .brand-name {
    font-family: "Montserrat", sans-serif;
    font-weight: 700;
    text-transform: uppercase;
    text-align: center;
    line-height: 1.05;
  }
  .card-front .brand-name {
    color: #ffffff;
    font-size: 30px;
    letter-spacing: 1px;
  }
  .card-front .brand-name span { display: block; font-size: 13px; letter-spacing: 7px; margin-top: 6px; }

  /* Back */
  .card-back {
    left: 466px; top: 460px; width: 608px; height: 250px;
    background: var(--card-white);
    overflow: hidden;
  }
  .contact-block { position: absolute; left: 58px; top: 60px; }
  .person-name {
    font-family: "Montserrat", sans-serif; font-weight: 700;
    font-size: 14px; letter-spacing: 1px; color: var(--ink);
    text-transform: uppercase;
  }
  .person-role {
    font-family: "Questrial", sans-serif; font-size: 12px;
    color: var(--ink-soft); margin-top: 2px;
  }
  .contact-list { list-style: none; margin-top: 20px; }
  .contact-list li {
    display: flex; align-items: center; gap: 8px;
    font-family: "Questrial", sans-serif; font-size: 12px;
    color: var(--ink-soft); height: 15px;
  }
  .contact-list svg { width: 11px; height: 11px; flex: none; }
  .address {
    font-family: "Questrial", sans-serif; font-size: 12px;
    color: var(--ink-soft); line-height: 1.5; margin-top: 16px;
  }

  .card-back .brand-name {
    position: absolute; left: 330px; top: 96px;
    color: var(--brand-red); font-size: 26px;
  }
  .card-back .brand-name span {
    display: block; font-size: 12px; letter-spacing: 6px; margin-top: 5px;
    padding-top: 3px; border-top: 1px solid var(--rule-grey);
  }

  .card-band { position: absolute; left: 0; bottom: 0; width: 608px; height: 20px; }
</style>
</head>
<body>
<main class="canvas">
  <section class="card card-front" aria-label="Card front">
    <p class="brand-name">Quelmira<span>Industries</span></p>
  </section>

  <section class="card card-back" aria-label="Card back">
    <div class="contact-block">
      <h1 class="person-name">Maren Tollis</h1>
      <p class="person-role">General Manager</p>
      <ul class="contact-list">
        <li>
          <svg viewBox="0 0 12 12"><circle cx="6" cy="6" r="5.5" fill="none" stroke="#8c2a2c"/><path d="M4 3.2l1 1.2-.6.8a4 4 0 0 0 1.9 1.9l.8-.6 1.2 1-.6.9C5.6 8.3 3.7 6.4 3.1 4.3z" fill="#8c2a2c"/></svg>
          (555) 014-2231
        </li>
        <li>
          <svg viewBox="0 0 12 12"><circle cx="6" cy="6" r="5.5" fill="none" stroke="#8c2a2c"/><rect x="3.2" y="5" width="5.6" height="3" fill="#8c2a2c"/><rect x="4.2" y="3" width="3.6" height="2" fill="none" stroke="#8c2a2c" stroke-width=".8"/></svg>
          (555) 014-2290
        </li>
        <li>
          <svg viewBox="0 0 12 12"><circle cx="6" cy="6" r="5.5" fill="none" stroke="#8c2a2c"/><rect x="3" y="4" width="6" height="4" fill="#8c2a2c"/><path d="M3 4l3 2.2L9 4" stroke="#fff" stroke-width=".7" fill="none"/></svg>
          info@quelmiraind.com
        </li>
        <li>
          <svg viewBox="0 0 12 12"><circle cx="6" cy="6" r="5.5" fill="#8c2a2c"/><ellipse cx="6" cy="6" rx="2.2" ry="4.5" fill="none" stroke="#fff" stroke-width=".7"/><path d="M1.5 6h9M2.3 4h7.4M2.3 8h7.4" stroke="#fff" stroke-width=".6"/></svg>
          www.quelmiraind.com
        </li>
      </ul>
      <p class="address">418 Larkspur Avenue<br>Suite 210, Brellton</p>
    </div>

    <p class="brand-name">Quelmira<span>Industries</span></p>

    <svg class="card-band" viewBox="0 0 608 20" preserveAspectRatio="none" aria-hidden="true">
      <polygon points="0,12 250,12 250,20 0,20" fill="var(--band-grey)"/>
      <polygon points="258,6 608,0 608,20 250,20" fill="var(--brand-red)"/>
    </svg>
  </section>
</main>
</body>
</html>
```